Business Cards for an 'affordable luxury' inner city home builder in Calgary.

We need a business card design that emulates the progressive, innovative, culture of our company and the modern style of our homes. Use our website www.velmarbuilds-ex.com as a reference for the product we build.

Our company builds homes in the inner city space of Calgary, Alberta. We build affordable luxury.

Target Market(s)

Young professional Families

Contact Information for Business Card

Try to maintain consistency with the logo font and the card font.

Requirements
Must have
• The details must include: Name, education, title, phone number, website and email (Address is not as important)
• The design must be uniques (like our logo), elegant, sophisticated and modern.

```html
<!DOCTYPE html>
<html lang="en">
<head>
<meta charset="utf-8">
<title>Velmar Custom Homes – Business Card</title>
<link rel="stylesheet" href="https://fonts.googleapis.com/css2?family=Lato:wght@700&family=Open+Sans:wght@400;600&display=swap">
<style>
  :root {
    --backdrop: #e8e5e1;
    --card-dark: #222222;
    --card-light: #f4f4f5;
    --text-light: #ffffff;
    --text-soft: #e6e6e6;
    --rule: #6c6c6c;
    --ink: #1e1e1e;
    --mark: #9a9a9a;
  }
  * { margin: 0; padding: 0; box-sizing: border-box; }
  html, body {
    width: 1200px; height: 900px; overflow: hidden;
    background: var(--backdrop);
  }
  .canvas { position: relative; width: 1200px; height: 900px; }
  .card {
    position: absolute; left: 330px; width: 556px; height: 343px;
    box-shadow: 2px 3px 6px rgba(0,0,0,0.25);
  }
  .card--back { top: 90px; background: var(--card-dark); color: var(--text-light); text-align: center; }
  .card--front { top: 469px; background: var(--card-light); }

  .holder-name {
    position: absolute; top: 107px; left: 0; width: 100%;
    font-family: "Lato", sans-serif; font-weight: 700; font-size: 21px; letter-spacing: 0.2px;
  }
  .holder-title {
    position: absolute; top: 128px; left: 0; width: 100%;
    font-family: "Open Sans", sans-serif; font-size: 15.5px; color: var(--text-soft);
  }
  .divider {
    position: absolute; top: 158px; left: 179px; width: 196px; height: 1px; background: var(--rule);
  }
  .contact-list {
    position: absolute; top: 170px; left: 0; width: 100%; list-style: none;
    font-family: "Open Sans", sans-serif; font-size: 15.5px; line-height: 20.5px; color: var(--text-soft);
  }
  .contact-list b { font-weight: 600; color: var(--text-light); }

  .brand {
    position: absolute; top: 134px; left: 100px; display: flex; align-items: center; gap: 26px;
  }
  .brand-square { width: 60px; height: 60px; background: var(--mark); }
  .brand-name {
    font-family: "Lato", sans-serif; font-weight: 700; font-size: 29px; line-height: 31px;
    letter-spacing: 1.5px; color: var(--ink); text-transform: uppercase;
  }
</style>
</head>
<body>
<main class="canvas">
  <section class="card card--back">
    <h1 class="holder-name">ADRIAN KESSLER</h1>
    <p class="holder-title">Managing Director</p>
    <div class="divider"></div>
    <ul class="contact-list">
      <li><b>P:</b> 044-555 010 274</li>
      <li><b>E:</b> info@velmarbuilds-ex.com</li>
      <li><b>W:</b> www.velmarbuilds-ex.com</li>
    </ul>
  </section>

  <section class="card card--front">
    <div class="brand">
      <span class="brand-square"></span>
      <p class="brand-name">Velmar<br>Custom<br>Homes Ltd</p>
    </div>
  </section>
</main>
</body>
</html>
```